A golden web-design opportunity

I have created a quick website (www.verimtrasystems.com.au) but I would like to have the website “polished” to look more professional and have a better consistency.

I would like the website to come across as a genuine, professional insight into our business culture but unfortunately my creative skills have reached their limit.

I have attached a media kit PDF so you are better able to establish what are about.
Updates

Hello All! I just wanted to let everyone know that I do not require an ecommerce site! My website is for potential clients to visit, see what we do and get my contact details...

Gathering more feedback

Hello All, I just wanted to let contestants know that there is not a requirement for my team to be mentioned on the website. I cover in person this as part of my presentation with clients. I have uploaded a new Presentation PDF that has this information excluded. Have a good day!

Target Market(s)

Telecommunications professionals; service delivery partners; white collar executives; construction

Industry/Entity Type

Data Communication

Coding

Coded - Design and coding required

Number of Pages Required

3 page

Font styles to use
Other font styles liked:
• Designers discretion

Colors

Designer to choose colors to be used in the design.

Requirements
Must have
• Must be designed so that I can upload it to Plesk, I think that wordpress is preferred.
• - Page:
• - 1 - Full page is a requirement i.e. the website makes full use of the whole screen
• - 2 - Colour scheme must be "muted" and not agressive
• - Links:
• - 1 - All links will work e.g. "E-Mail us" should work
• - 2 - The page identifier ("[LOGO] Home | Verimtra Sytsems) will show the Verimtra logo
• - 3 - A link to facebook and linkedin
• - https://www.facebook.com/verimtrasystems
• - https://www.linkedin.com/company/verimtra-systems-pty-ltd/
• - 4 - The phone number icon can be clicked on to make a call
• - 5 - The E-Mail icon can be clicked on to send an E-Mail
Nice to have
• Font:
• - 1 - Rounded is preferred
• - 2 - Colour with reference the logo colours (if possible)
Should not have
• Colour:
• - 1 - To much contrast between colours i.e. balck background with white writing
• - 2 - aggressive colour schemes
• - 3 - Names of Verimtra consultants... These guys are also used by my competetion, only martin is required

```html
<!DOCTYPE html>
<html lang="en">
<head>
<meta charset="utf-8">
<title>Home | Verimtra Solutions</title>
<link href="https://fonts.googleapis.com/css2?family=Poppins:wght@300;400;500;600;700&display=swap" rel="stylesheet">
<style>
:root{
  --navy:#0b1a3a;
  --navy-deep:#07122b;
  --teal:#1f8fbf;
  --teal-dark:#167aa6;
  --blue-text:#1a3f8f;
  --ink:#2f3a4a;
  --muted:#6b7686;
  --line:#d8dee6;
  --paper:#ffffff;
  --mist:#f4f6f9;
}
*{box-sizing:border-box;margin:0;padding:0}
html,body{width:1200px;height:3220px;overflow:hidden}
body{font-family:"Poppins",sans-serif;color:var(--ink);background:var(--paper);position:relative}
.abs{position:absolute}

/* top bar + header */
.topbar{position:absolute;top:0;left:0;width:1200px;height:30px;background:rgba(8,18,40,.85);display:flex;justify-content:flex-end;align-items:center;gap:18px;padding-right:110px;font-size:11px;color:#fff;z-index:3}
.topbar .mail{display:flex;align-items:center;gap:8px;margin-right:20px}
.topbar .dot{width:10px;height:10px;border-radius:50%;background:#fff}
.header{position:absolute;top:30px;left:0;width:1200px;height:62px;background:#fff;display:flex;align-items:center;z-index:3;box-shadow:0 2px 6px rgba(0,0,0,.08)}
.logo{position:absolute;left:132px;display:flex;align-items:center;gap:10px;font-size:26px;font-weight:600;color:var(--blue-text);letter-spacing:.5px}
.logo .mark{width:42px;height:42px;border-radius:50%;background:var(--teal)}
.nav{position:absolute;left:570px;display:flex;gap:40px;font-size:12.5px;color:var(--muted);letter-spacing:.5px}
.nav .active{color:var(--teal);position:relative}
.nav .active::after{content:"";position:absolute;left:-6px;right:-6px;top:-22px;height:3px;background:var(--teal)}
.btn-enquiry{position:absolute;left:980px;width:116px;height:40px;border:2px solid var(--teal);border-radius:20px;color:var(--teal);font-size:12.5px;display:flex;align-items:center;justify-content:center}

/* hero */
.hero{position:absolute;top:0;left:0;width:1200px;height:690px;overflow:hidden}
.hero-photo{position:absolute;inset:0;background:linear-gradient(160deg,#9ba7b3 0%,#6d7885 40%,#3d4652 75%,#2a313a 100%)}
.hero-shade{position:absolute;inset:0;background:rgba(15,25,40,.35)}
.hero h1{position:absolute;top:255px;width:100%;text-align:center;font-size:56px;color:#fff;font-weight:700;letter-spacing:1px}
.hero h1 span{font-weight:400}
.hero .tagline{position:absolute;top:360px;width:100%;text-align:center;font-size:28px;color:#fff;font-weight:400}
.btn{display:flex;align-items:center;justify-content:center;background:var(--teal);color:#fff;border-radius:24px;font-size:13px;letter-spacing:.5px}
.hero .btn{position:absolute;left:526px;top:450px;width:148px;height:46px}
.slide-arrow{position:absolute;top:316px;width:40px;height:38px;background:rgba(255,255,255,.25);display:flex;align-items:center;justify-content:center}
.slide-arrow.right{right:0;background:#fff}
.hero-curve{position:absolute;left:0;top:470px}

/* story */
.story-photo{position:absolute;left:98px;top:785px;width:320px;height:320px;border-radius:50%;background:radial-gradient(circle at 45% 40%,#bfe3f5 0%,#3d8fc2 35%,#134a7c 70%,#0a2b52 100%);border:10px solid var(--teal);box-shadow:0 0 0 4px #fff inset}
.story-tail{position:absolute;left:80px;top:1080px}
.eyebrow{font-size:12px;color:var(--teal);letter-spacing:1px;text-transform:uppercase}
.story{position:absolute;left:612px;top:752px;width:470px}
.story h2{margin-top:20px;font-size:24px;font-weight:500;color:var(--blue-text);line-height:1.45}
.story p{margin-top:16px;font-size:13px;line-height:1.75;color:var(--muted)}
.tags{display:flex;gap:10px;margin-top:26px}
.tags span{width:140px;height:30px;border:1.5px solid var(--teal);display:flex;align-items:center;justify-content:center;font-size:11px;color:var(--teal)}
.story .btn{width:148px;height:48px;margin-top:34px}

/* services */
.services-bg{position:absolute;left:0;top:1280px}
.services{position:absolute;left:0;top:1336px;width:1200px;text-align:center;color:#fff}
.services h2{font-size:22px;font-weight:600;margin-top:14px;letter-spacing:.5px}
.services .intro{font-size:12.5px;line-height:1.9;margin-top:30px;color:#d7dfe9}
.cards{position:absolute;left:125px;top:1557px;width:950px;display:grid;grid-template-columns:repeat(4,215px);gap:32px 30px}
.card{height:156px;background:#fff;display:flex;flex-direction:column;align-items:center;justify-content:flex-end;padding-bottom:22px}
.card .ico{width:64px;height:64px;border-radius:8px;margin-bottom:20px}
.card .name{font-size:12px;color:var(--ink);letter-spacing:.3px}
.card .name b{font-weight:400;color:var(--teal)}
.services-more{position:absolute;top:1935px;width:1200px;text-align:center;color:#fff}
.services-more p{font-size:12.5px;color:#d7dfe9}
.services-more h3{font-size:22px;font-weight:400;margin-top:30px}
.services-more .btn{width:150px;height:50px;margin:22px auto 0}

/* enquiry */
.enquiry-head{position:absolute;top:2186px;width:1200px;text-align:center}
.enquiry-head h2{margin-top:14px;font-size:22px;font-weight:600;color:var(--blue-text);letter-spacing:.5px}
.enquiry-copy{position:absolute;left:125px;top:2300px;width:440px;font-size:13.5px;line-height:1.75;color:var(--ink)}
.enquiry-copy p+p{margin-top:12px}
.contact-box{position:absolute;top:2432px;height:52px;border:2px solid var(--teal);display:flex;align-items:center}
.contact-box .ic{width:52px;height:100%;background:var(--teal);display:flex;align-items:center;justify-content:center}
.contact-box .val{padding-left:14px;color:var(--teal)}
.map{position:absolute;left:125px;top:2501px;width:463px;height:236px;background:linear-gradient(135deg,#eef0e6,#e4e8dc 50%,#f2e6c8)}
.form{position:absolute;left:610px;top:2306px;width:464px;height:436px;background:#fff;box-shadow:0 2px 12px rgba(0,0,0,.14);border-radius:4px;padding:30px 34px}
.form label{display:block;font-size:11.5px;color:var(--ink);margin-bottom:8px}
.field{height:40px;border:1px solid var(--line)}
.row{display:grid;grid-template-columns:1fr 1fr;gap:10px}
.group{margin-bottom:18px}
.select{display:flex;align-items:center;justify-content:space-between;padding:0 18px 0 12px;font-size:12px}
.textarea{height:70px}
.form .btn{width:116px;height:40px;font-size:12px;margin-top:6px}

/* footer */
.footer-bg{position:absolute;left:0;top:2800px}
.footer{position:absolute;top:2895px;left:0;width:1200px;color:#fff}
.col{position:absolute;top:0}
.col h4{font-size:12.5px;font-weight:500;letter-spacing:.5px;margin-bottom:26px}
.col li{list-style:none;font-size:11.5px;color:#d7dfe9;margin-bottom:12px}
.info{display:flex;gap:14px;margin-bottom:18px;font-size:11px;color:#d7dfe9;line-height:1.6}
.info b{display:block;color:#fff;font-weight:600}
.socials{display:flex;gap:14px}
.socials span{width:40px;height:40px;border-radius:50%;background:#fff}
.newsletter{margin-top:34px;font-size:12.5px;font-weight:500;letter-spacing:.5px}
.subscribe{margin-top:30px;display:flex;width:305px;height:32px;border:1px solid #8a94a6}
.subscribe .in{flex:1;font-size:10px;color:#9aa4b4;display:flex;align-items:center;padding-left:14px}
.subscribe .go{width:85px;background:#5b6576;font-size:10px;display:flex;align-items:center;justify-content:center}
.copyright{position:absolute;top:3178px;left:0;width:1200px;height:42px;background:#fff;text-align:center;font-size:11px;color:var(--ink);line-height:42px}
.notch{position:absolute;left:590px;top:3178px;width:0;height:0;border-left:10px solid transparent;border-right:10px solid transparent;border-top:10px solid var(--navy)}
</style>
</head>
<body>

<section class="hero">
  <div class="hero-photo" role="img" aria-label="Photo of people working at laptops and taking notes on a desk"></div>
  <div class="hero-shade"></div>
  <h1>VERIMTRA <span>SOLUTIONS</span></h1>
  <div class="tagline">Project Delivery. Done Differently</div>
  <a class="btn">FIND OUT MORE</a>
  <div class="slide-arrow left"><svg width="10" height="14"><path d="M8 1 2 7l6 6" stroke="#fff" stroke-width="2" fill="none"/></svg></div>
  <div class="slide-arrow right"><svg width="10" height="14"><path d="M2 1l6 6-6 6" stroke="#222" stroke-width="2" fill="none"/></svg></div>
  <svg class="hero-curve" width="1200" height="220" viewBox="0 0 1200 220">
    <path d="M0 60 Q560 250 1200 20 L1200 220 L0 220Z" fill="#fff"/>
    <path d="M700 158 Q980 120 1200 20 L1200 58 Q990 150 760 172 Z" fill="var(--teal)"/>
    <path d="M960 140 L1030 178 L1040 130Z" fill="var(--teal)"/>
  </svg>
</section>

<div class="topbar">
  <span class="mail"><span class="dot"></span>hello@verimtrasystems.com.au</span>
  <span class="dot"></span><span class="dot"></span><span class="dot"></span>
</div>
<header class="header">
  <div class="logo"><span class="mark"></span>VERIMTRA</div>
  <nav class="nav">
    <span class="active">HOME</span><span>OUR STORY</span><span>SERVICES</span><span>CONTACTS</span>
  </nav>
  <a class="btn-enquiry">ENQUIRY</a>
</header>

<section>
  <svg class="story-tail" width="120" height="120"><path d="M40 20 L20 112 L110 70Z" fill="var(--teal)"/></svg>
  <div class="story-photo" role="img" aria-label="Illustration of a hand holding a glowing laptop surrounded by digital communication icons"></div>
  <div class="story">
    <div class="eyebrow">Our Story</div>
    <h2>We are an innovative<br>telecommunications services company.</h2>
    <p>We believe technology can truly change peoples' lives, so we are working with Victoria's most respected delivery partners to complete unique projects state-wide.</p>
    <p>We are focusing on three key areas that we hope will build our distinct brand within the Australian telecommunications industry.</p>
    <div class="tags"><span>INNOVATION</span><span>COLLABORATION</span><span>INTEGRITY</span></div>
    <a class="btn">KNOW MORE</a>
  </div>
</section>

<section>
  <svg class="services-bg" width="1200" height="850" viewBox="0 0 1200 850">
    <defs><linearGradient id="svcGrad" x1="0" y1="0" x2="0" y2="1"><stop offset="0" stop-color="#0c1c3e"/><stop offset="1" stop-color="#07122b"/></linearGradient></defs>
    <path d="M0 50 Q600 -30 1200 50 L1200 790 Q600 880 0 790Z" fill="url(#svcGrad)"/>
  </svg>
  <div class="services">
    <div class="eyebrow">What We Offer</div>
    <h2>WE ARE PROVIDING MULTIPLE SERVICES</h2>
    <p class="intro">Working with VerimtraSolutions enables a single point of contact for your entire project. We have a wide range of specialties and<br>in-house capabilities that allows us to take on full responsibility for projects.</p>
    <p class="intro" style="margin-top:10px">Working with Verimtra Solutions reduces clients' deployment costs and time to complete the project.</p>
  </div>
  <div class="cards">
    <div class="card"><div class="ico" role="img" aria-label="Project management illustration" style="background:#d6e9f3"></div><div class="name">PROJECT <b>MANAGEMENT</b></div></div>
    <div class="card"><div class="ico" role="img" aria-label="Asbestos removal tool illustration" style="background:#f3d8d8"></div><div class="name">ASBESTOS <b>REMOVAL</b></div></div>
    <div class="card"><div class="ico" role="img" aria-label="Pit and pipe illustration" style="background:#e6e8ec"></div><div class="name">PIT AND PIPE <b>INSTALLATION</b></div></div>
    <div class="card"><div class="ico" role="img" aria-label="Cable hauling illustration" style="background:#e8e3dc"></div><div class="name">CABLE <b>HAULING</b></div></div>
    <div class="card"><div class="ico" role="img" aria-label="Fibre splicing illustration" style="background:#f1dcd8"></div><div class="name">FIBRE <b>SPLICING</b></div></div>
    <div class="card"><div class="ico" role="img" aria-label="Copper jointing pliers illustration" style="background:#f3dcd6"></div><div class="name">COPPER <b>JOINTING</b></div></div>
    <div class="card"><div class="ico" role="img" aria-label="Fibre integration cable illustration" style="background:#dbe3ee"></div><div class="name">FIBRE <b>INTEGRATION</b></div></div>
    <div class="card"><div class="ico" role="img" aria-label="Tele rigging tower illustration" style="background:#f1dcdc"></div><div class="name">TELE <b>RIGGING</b></div></div>
  </div>
  <div class="services-more">
    <p>Verimtra solutions has a diverse range of skills, experience and capabilities.</p>
    <h3>For more details contact us today</h3>
    <a class="btn">CONTACT US</a>
  </div>
</section>

<section>
  <div class="enquiry-head">
    <div class="eyebrow">Get Enquiry</div>
    <h2>CONNECT WITH VERIMTRA SOLUTIONS</h2>
  </div>
  <div class="enquiry-copy">
    <p>Verimtra Solutions understands business and we take pride in helping Victorian businesses meet their goals.</p>
    <p>Let Verimtra Solutions be part of your business's journey, call us today</p>
  </div>
  <a class="contact-box" style="left:125px;width:215px">
    <span class="ic"><svg width="24" height="24" viewBox="0 0 24 24"><path d="M6.6 10.8a15 15 0 0 0 6.6 6.6l2.2-2.2a1 1 0 0 1 1-.25 11.4 11.4 0 0 0 3.6.57 1 1 0 0 1 1 1V20a1 1 0 0 1-1 1A17 17 0 0 1 3 4a1 1 0 0 1 1-1h3.5a1 1 0 0 1 1 1c0 1.25.2 2.45.57 3.57a1 1 0 0 1-.25 1Z" fill="#fff"/></svg></span>
    <span class="val" style="font-size:16px">+61 400 555 218</span>
  </a>
  <a class="contact-box" style="left:348px;width:240px">
    <span class="ic"><svg width="26" height="20" viewBox="0 0 26 20"><rect x="1" y="1" width="24" height="18" fill="none" stroke="#fff" stroke-width="2"/><path d="M1 1l12 10L25 1" fill="none" stroke="#fff" stroke-width="2"/></svg></span>
    <span class="val" style="font-size:10.5px">info@verimtrasystems.com.au</span>
  </a>
  <div class="map" role="img" aria-label="Street map of eastern Melbourne suburbs with a location pin"></div>
  <div class="form">
    <div class="row group"><div><label>Name</label><div class="field"></div></div><div><label>Phone</label><div class="field"></div></div></div>
    <div class="group"><label>Email</label><div class="field"></div></div>
    <div class="group"><label>How did you find us?</label><div class="field select">Found on a search engine <svg width="10" height="6"><path d="M0 0h10L5 6Z" fill="#222"/></svg></div></div>
    <div class="group"><label>Message</label><div class="field textarea"></div></div>
    <a class="btn">SUBMIT</a>
  </div>
</section>

<footer>
  <svg class="footer-bg" width="1200" height="380" viewBox="0 0 1200 380">
    <path d="M0 40 Q600 -20 1200 40 L1200 380 L0 380Z" fill="var(--navy)"/>
  </svg>
  <div class="footer">
    <div class="col" style="left:118px;width:260px">
      <h4>PLACE INFORMATION</h4>
      <div class="info"><svg width="18" height="16"><path d="M9 1 1 8h2v7h4v-5h4v5h4V8h2Z" fill="#fff"/></svg><div><b>ADDRESS:</b>42 Harbour Lane #200<br>Ringwood, VIC 3134</div></div>
      <div class="info"><svg width="18" height="16" viewBox="0 0 24 24"><path d="M6.6 10.8a15 15 0 0 0 6.6 6.6l2.2-2.2a1 1 0 0 1 1-.25 11.4 11.4 0 0 0 3.6.57 1 1 0 0 1 1 1V20a1 1 0 0 1-1 1A17 17 0 0 1 3 4a1 1 0 0 1 1-1h3.5a1 1 0 0 1 1 1c0 1.25.2 2.45.57 3.57a1 1 0 0 1-.25 1Z" fill="#fff"/></svg><div><b>MOBILE:</b>707-555-0142</div></div>
      <div class="info"><svg width="18" height="14"><rect x="1" y="1" width="16" height="12" fill="none" stroke="#fff" stroke-width="1.6"/><path d="M1 1l8 6 8-6" fill="none" stroke="#fff" stroke-width="1.6"/></svg><div><b>EMAIL:</b>info@verimtrasystems.com.au</div></div>
    </div>
    <div class="col" style="left:393px">
      <h4>QUICK LINKS</h4>
      <ul><li>Home</li><li>About Us</li><li>Our Services</li><li>Enquiry</li></ul>
    </div>
    <div class="col" style="left:584px">
      <h4>CUSTOMER SERVICE</h4>
      <ul><li>Contact Us</li><li>RSS</li><li>Help &amp; FAQs</li><li>Consultant</li><li>Store Locations</li></ul>
    </div>
    <div class="col" style="left:779px">
      <h4>STAY CONNECTED</h4>
      <div class="socials"><span></span><span></span><span></span></div>
      <div class="newsletter">SUBSCRIBE IN OUR NEWS LETTER</div>
      <div class="subscribe"><span class="in">Enter Your Email Address</span><span class="go">SUBSCRIBE</span></div>
    </div>
  </div>
  <div class="copyright">© 2018 &nbsp;Verimtra Solutions. All Rights Reserved.</div>
  <div class="notch"></div>
</footer>

</body>
</html>
```